依頼詳細
A社より添付の案を頂いているのですが、①グループ会社である安心感親近感をアピールしたい②メリット1のA社専用のプランを他のメリットよりも強調したいと思い、依頼をさせて頂く事となりました。
注意点、会社案内欄の箇所は空白でお願い致します。
社名を変更して今後活用したいので、パワーポイントでの納品をお願い致します。
記載項目
株式会社ZAT/03-4817-2935/https://www.za-t.jp/
サイズ
A4
ページ数
片面
希望イメージ
シンプル 複雑
単色 カラフル
暗い 明るい
日常 高級
遊び心 厳粛
未来的 伝統的
女性的 男性的
希望する色
納品ファイル
補足説明
■ 選んだ理由

社員の選定を元に選ばせて頂きました。親近感があるという意見が多かったです。

■ 提案者全員のお礼・コメント

締め切りが近い中多数のご応募頂きありがとうございます。またご機会ありましたら宜しくお願い致します。

```html
<!DOCTYPE html>
<html lang="ja">
<head>
<meta charset="utf-8">
<title>専用火災保険のご案内</title>
<link rel="stylesheet" href="https://fonts.googleapis.com/css2?family=Noto+Sans+JP:wght@400;500;700&family=Noto+Serif+JP:wght@500;600;700;900&display=swap">
<style>
:root{
  --gold:#b8965a;
  --gold-light:#e9dcc0;
  --gold-pale:#f6efe0;
  --gold-deep:#8f7038;
  --ink:#2e2a26;
  --brown:#4a3b2c;
  --red:#b3261e;
  --grey:#9a9a9a;
  --grey-pale:#efefef;
  --white:#ffffff;
}
*{margin:0;padding:0;box-sizing:border-box}
html,body{width:849px;height:1200px;overflow:hidden;background:var(--white)}
body{font-family:"Noto Sans JP",sans-serif;color:var(--ink);position:relative}
.issue-note{position:absolute;top:14px;right:36px;font-size:12px;color:var(--ink)}
.hero{position:absolute;top:36px;left:0;width:849px;height:392px;
  background:linear-gradient(180deg,#f3ead8 0%,#e7d6b3 55%,#d9c293 100%);overflow:hidden}
.hero-photo{position:absolute;right:20px;top:20px;width:260px;height:372px;
  background:linear-gradient(180deg,#e4e1dc 0%,#c9c6c1 60%,#a9a6a2 100%);border-radius:4px 4px 0 0}
.hero-intro{position:absolute;left:80px;top:36px;width:430px;background:var(--brown);
  color:var(--white);font-family:"Noto Serif JP",serif;font-size:17px;line-height:1.75;
  text-align:center;padding:12px 10px;letter-spacing:.02em}
.hero-title{position:absolute;left:40px;top:150px;width:520px;text-align:center;
  font-family:"Noto Serif JP",serif;color:var(--ink)}
.hero-title .from{font-size:40px;font-weight:600}
.hero-title .main{font-size:74px;font-weight:700;letter-spacing:.04em;line-height:1.2}
.hero-title .tail{font-size:38px;font-weight:600}
.plan-band{position:absolute;top:450px;left:36px;width:777px;height:54px;
  background:linear-gradient(90deg,var(--gold-deep),var(--gold),var(--gold-deep));
  color:var(--white);font-family:"Noto Serif JP",serif;font-weight:700;font-size:28px;
  display:flex;align-items:center;justify-content:center;letter-spacing:.03em}
.price-box{position:absolute;top:504px;left:36px;width:777px;height:98px;
  border:2px solid var(--gold);border-top:none;background:var(--white);
  display:flex;align-items:center;justify-content:center;gap:14px;font-family:"Noto Serif JP",serif}
.price-box .accent{color:var(--red);font-size:50px;font-weight:900;letter-spacing:.04em}
.price-box .rest{display:flex;flex-direction:column;font-size:28px;font-weight:700}
.price-box .rest small{font-size:13px;font-weight:500}
.points{position:absolute;top:630px;left:36px;width:777px;display:grid;
  grid-template-columns:1fr 1fr;column-gap:28px;row-gap:26px}
.point{border-top:1px solid var(--gold-light);padding-top:14px;height:210px;position:relative}
.point-head{display:flex;gap:12px;align-items:flex-start}
.badge{width:58px;height:64px;flex:none;background:var(--gold-pale);border:1px solid var(--gold);
  display:flex;flex-direction:column;align-items:center;justify-content:center;color:var(--gold-deep)}
.badge span{font-size:9px}
.badge b{font-family:"Noto Serif JP",serif;font-size:30px;line-height:1}
.point-title{font-family:"Noto Serif JP",serif;font-weight:700;font-size:25px;line-height:1.35}
.point-text{font-size:12px;margin-top:18px;line-height:1.7;color:var(--ink)}
.stats{margin-top:18px;width:100%;border-collapse:collapse;font-size:12px}
.stats td{padding:3px 0}
.stats .num{text-align:right;color:var(--red);font-size:17px;font-weight:700;font-family:"Noto Serif JP",serif}
.footer-space{position:absolute;left:0;bottom:0;width:849px;height:96px;background:var(--grey-pale);
  display:flex;align-items:center;justify-content:center;color:var(--grey);font-size:22px;letter-spacing:.08em}
</style>
</head>
<body>
<p class="issue-note">0000年00月以降保険始期用</p>

<section class="hero">
  <div class="hero-photo" role="img" aria-label="スーツ姿の女性スタッフの写真"></div>
  <p class="hero-intro">「ダミー」の住宅購入されるお客様へ<br>「ダミー」より下記提携代理店をご紹介します。</p>
  <h1 class="hero-title">
    <span class="from">「ダミー」より</span><br>
    <span class="main">専用火災保険</span><br>
    <span class="tail">のご案内です。</span>
  </h1>
</section>

<div class="plan-band">「ダミー」オーナー様 専用プラン適用!</div>
<div class="price-box">
  <span class="accent">割安な保険料</span>
  <span class="rest"><small>(地震保険は除く)</small>でご利用いただけます。</span>
</div>

<section class="points">
  <article class="point">
    <div class="point-head">
      <div class="badge"><span>ポイント</span><b>1</b></div>
      <h2 class="point-title">ご契約時お建物資料等の<br>ご提出不要!</h2>
    </div>
    <p class="point-text">「ダミー」と「ダミー」で直接やりとりいたします。</p>
  </article>
  <article class="point">
    <div class="point-head">
      <div class="badge"><span>ポイント</span><b>2</b></div>
      <h2 class="point-title">「ダミー」は<br>火災保険専門代理店</h2>
    </div>
    <table class="stats">
      <tr><td>2019年度お取扱実績</td><td class="num">3,500件</td></tr>
      <tr><td>2020年6月現在保有契約件数</td><td class="num">28,000件</td></tr>
    </table>
    <p class="point-text" style="margin-top:10px">火災保険専門でございますのでお客様にわかりやすくご案内させていただきます。</p>
  </article>
  <article class="point">
    <div class="point-head">
      <div class="badge"><span>ポイント</span><b>3</b></div>
      <h2 class="point-title">土日祝日も<br>ご案内いたします!</h2>
    </div>
    <p class="point-text">お客様のご都合の良い日時にご案内させていただきます。</p>
  </article>
  <article class="point">
    <div class="point-head">
      <div class="badge"><span>ポイント</span><b>4</b></div>
      <h2 class="point-title">スピーディーな<br>お申込み手続き!</h2>
    </div>
    <p class="point-text">最短で当日から補償開始のお手続きが可能です。</p>
  </article>
</section>

<footer class="footer-space">注意点・会社案内欄</footer>
</body>
</html>
```